Tidewell Works's Facebook Cover Design

I am in need of a social media cover for my company's Facebook account. Please leverage the green logos and color palette attached.

Tidewell Works offers 2 primary services:
1.) Business Automation Services
2.) AI (artificial intelligence integrations)

While a lot of what we do is highly technical, what we deliver is not. In a nutshell, we help our clients to connect their data regardless of what application that data is sitting in. Because we can connect that data, often times we can:

A.) offer more intelligent marketing and help our client increase their revenue.
B.) automate highly repetitive tasks using technology and drive down their costs thus saving them money
C.) help our clients use AI to better serve their customers

You can read a little bit about our company here: https://www.tidewellworks.example

Our tagline is: "Connect data to increase the flow of profitability."

Visually, we'd like your help to illustrate the "connecting" of these applications. Please let me know if you have any questions.

Target Market(s)

Business Owners or Marketing Managers

Industry/Entity Type

Marketing technologies.

Font styles to use
Sans Serif

Requirements
Must have
• Please make every effort to have the cover compatible with the color palette of the attached images.
Should not have
• Please do not use the standard clipart or stock libraries of AI = robot. If you do, please make them small. We help business glue their data from different sources to solve real work problems. Little robots are overused.

```html
<!DOCTYPE html>
<html lang="en">
<head>
<meta charset="utf-8">
<title>Tidewell Works – Facebook Cover</title>
<link rel="stylesheet" href="https://fonts.googleapis.com/css2?family=Signika:wght@400;600;700&display=swap">
<style>
  :root {
    --backdrop: #8b8b8b;
    --paper: #ffffff;
    --ink: #4a4a4a;
    --green: #7cc142;
    --green-deep: #5fa62e;
    --slate: #4f5152;
  }
  * { margin: 0; padding: 0; box-sizing: border-box; }
  html, body { width: 1200px; height: 961px; overflow: hidden; background: var(--backdrop); }
  body { font-family: "Signika", sans-serif; }

  .sheet {
    position: relative; width: 937px; height: 750px;
    transform: scale(1.2807); transform-origin: 0 0;
  }
  .cover {
    position: absolute; left: 41px; width: 851px; height: 314px;
    background: var(--paper); overflow: hidden;
    box-shadow: 0 4px 12px rgba(0,0,0,.35);
  }
  .cover--angled { top: 39px; }
  .cover--curve { top: 394px; }
  .cover svg.art { position: absolute; inset: 0; width: 851px; height: 314px; }
  .line { position: absolute; white-space: nowrap; }

  /* angled cover */
  .tag-plain { font-size: 24px; color: var(--ink); font-weight: 400; }
  .tag-accent { font-size: 27px; color: var(--green); font-weight: 700; }
  .brand { font-weight: 700; color: var(--green); display: flex; align-items: center; gap: 5px; }
  .brand i { display: block; width: 8px; height: 8px; border-radius: 50%; background: var(--green); }
  .cover--angled .brand { left: 669px; top: 22px; font-size: 20px; }
  .offer { left: 623px; top: 68px; font-size: 20px; line-height: 28px; font-weight: 700; color: var(--ink); }
  .offer-list { font-size: 11.5px; color: var(--ink); font-weight: 600; }
  .call { left: 667px; top: 239px; font-size: 13px; color: var(--green); font-weight: 600; }
  .phone { left: 688px; top: 268px; display: flex; align-items: center; gap: 6px; font-size: 11px; font-weight: 700; color: var(--ink); }
  .phone svg { width: 24px; height: 24px; }

  /* curve cover */
  .cover--curve .brand { left: 43px; top: 20px; font-size: 28px; }
  .cover--curve .brand i { width: 11px; height: 11px; }
  .headline { left: 42px; font-size: 31px; font-weight: 700; color: var(--ink); letter-spacing: .3px; }
  .headline--accent { color: var(--green); }
  .services-title { left: 42px; top: 197px; font-size: 18px; font-weight: 700; color: var(--ink); }
  .services-rule { position: absolute; left: 42px; top: 224px; width: 32px; height: 2px; background: var(--green); }
  .service-item { left: 42px; font-size: 11.5px; color: var(--ink); text-transform: uppercase; }
</style>
</head>
<body>
<main class="sheet">

  <section class="cover cover--angled">
    <svg class="art" viewBox="0 0 851 314">
      <defs>
        <linearGradient id="photoTone" x1="0" y1="0" x2="1" y2="1">
          <stop offset="0" stop-color="#d8d2c8"/>
          <stop offset=".5" stop-color="#b49c86"/>
          <stop offset="1" stop-color="#6f6a66"/>
        </linearGradient>
        <linearGradient id="bandRise" x1="0" y1="1" x2="1" y2="0">
          <stop offset="0" stop-color="#7cc142"/>
          <stop offset=".55" stop-color="#6aa83a"/>
          <stop offset="1" stop-color="#4f5152"/>
        </linearGradient>
        <linearGradient id="bandFall" x1="0" y1="0" x2="0" y2="1">
          <stop offset="0" stop-color="#4f5152"/>
          <stop offset=".6" stop-color="#6aa83a"/>
          <stop offset="1" stop-color="#7cc142"/>
        </linearGradient>
      </defs>
      <polygon points="0,0 430,0 40,314 0,314" fill="url(#photoTone)" role="img" aria-label="Photo of two colleagues reviewing data on a tablet in an office"/>
      <polygon points="300,0 470,0 250,170" fill="#55585a" opacity=".85"/>
      <polygon points="30,314 130,314 530,0 430,0" fill="url(#bandRise)"/>
      <polygon points="490,0 570,0 660,314 590,314" fill="url(#bandFall)"/>
    </svg>

    <p class="line tag-plain" style="left:286px; top:200px;">CONNECT DATA</p>
    <p class="line tag-accent" style="left:239px; top:231px;">TO INCREASE THE FLOW</p>
    <p class="line tag-plain" style="left:215px; top:268px;">OF PROFITABILITY.</p>

    <p class="line brand"><i></i>Tidewell Works</p>
    <h2 class="line offer">TIDEWELL WORKS<br>OFFERS 2 PRIMARY<br>SERVICES:</h2>
    <p class="line offer-list" style="left:628px; top:162px;">1.) Business Automation Services</p>
    <p class="line offer-list" style="left:643px; top:184px;">2.) AI (artificial intelligence</p>
    <p class="line offer-list" style="left:656px; top:206px;">integrations)</p>
    <p class="line call">Call For More Details</p>
    <p class="line phone">
      <svg viewBox="0 0 24 24" aria-hidden="true">
        <circle cx="12" cy="12" r="12" fill="var(--green)"/>
        <path d="M9.2 6.5l1.6 2.6-1.1 1.3c.7 1.5 1.9 2.7 3.4 3.4l1.3-1.1 2.6 1.6-.6 2.1c-4.8-.3-8.6-4.1-8.9-8.9z" fill="#fff"/>
      </svg>
      +1555 0100 0000
    </p>
  </section>

  <section class="cover cover--curve">
    <svg class="art" viewBox="0 0 851 314">
      <defs>
        <linearGradient id="meetingTone" x1="0" y1="0" x2="1" y2="1">
          <stop offset="0" stop-color="#e3ddd2"/>
          <stop offset=".45" stop-color="#b8a58f"/>
          <stop offset="1" stop-color="#5d5f55"/>
        </linearGradient>
      </defs>
      <path d="M480 0 H851 V314 H450 C410 250 500 200 470 140 C445 90 470 40 480 0 Z" fill="url(#meetingTone)" role="img" aria-label="Photo of a team meeting around a table with laptops"/>
      <path d="M480 -5 C470 40 445 90 470 140 C500 200 410 250 450 320" fill="none" stroke="var(--green)" stroke-width="34" stroke-linecap="round"/>
    </svg>

    <p class="line brand"><i></i>Tidewell Works</p>
    <p class="line headline" style="top:70px;">CONNECT DATA TO</p>
    <p class="line headline headline--accent" style="top:106px;">INCREASE THE FLOW</p>
    <p class="line headline" style="top:142px;">OF PROFITABILITY.</p>
    <h3 class="line services-title">SERVICES</h3>
    <span class="services-rule"></span>
    <p class="line service-item" style="top:237px;">1.) Business Automation Services</p>
    <p class="line service-item" style="top:261px;">2.) AI (Artificial Intelligence Integrations)</p>
  </section>

</main>
</body>
</html>
```